FR / EN Beekeeper research design packaging / label; Beekeeper looking for a design package

I need as a beekeeper to create a design to better showcase my honey. Indeed I work in a natural environment of high quality on a hill called "Waldhofen" (many flowers different fields, few pesticides, ...). I practice a beekeeping respectful of the bee and in a traditional way. I produce a high quality honey (luxury product) for a wealthy clientele looking for good health products, ... The main label should contain only the following text (accompanied by an image): The Waldhofen Honey A variant would also be useful for my production of mead (alcohol from the fermentation of honey): The Waldhofen mead In terms of form, given the target audience, I thought I was moving towards a modern label against a background black and with golden patterns. An example is the honey of the wonders attached, we find a honey assimilated as a real luxury product. Same in the Cuvée Lorenzo Pavetti attachment. I would like to move towards these tones of colors by adding a touch more "champêtre" as on the label of the bottle of wine below where one sees golden flowers drawn, of light and subtle way. Another example that I like is that of the bee of ree joined. Another modern idea identified on this site is this design: https://www.artpitchhub.example/design/52817304 https: //www.artpitchhub. example / design / 52817391 I would also need a round label to place on the lid of the pot with indications of signs (my address) as well as additional information about my product: - VALENTE Gaspard - Waldhofen, 14 - 6812 Brouvelle - 500 g - Spring harvest - Honey all flowers - Flora: rapeseed, fruit trees, clovers - Flavors: sweet honey with vegetal notes Remarks: this is my first artpitchhub project, if you are surprised by some points of the brief or it is missing important information do not hesitate to let me know! ************************************************** ******************************* ENGLISH ****************** ************** I need to beekeeper a new design Indeed, I work in a very natural environment, a high quality eco-system which is the south of Belgium (many different flowers in the fields, few pesticides, ...). I practice a natural beekeeping, in an artisanal way I produce a high quality honey (luxuous product) for wealthy people who are looking for good and healthy products. The following description: The Waldhofen Honey A slight variation could be useful for my production (alcohol from honey fermentation): The Waldhofen Meads Concerning the form, a modern design with golden patterns on a black background could be appropriate. An example is the honey of the wonders in attachment, we could see that honey in this case is a branded like a very luxuous product. I wish to go for these last colors with a more "rural touch" as attachment. We can see golden flowers in a light and elegant manner. Another interesting example is the honey bee in attachment. Some example found on this site: https://www.artpitchhub.example/design/52817304 https: //www.artpitchhub. example / design / 52817391 Valente Gaspard - Waldhofen, 14 - 6812 Brouvelle - 500 g - Spring Harvest - Honey all flowers - Flora: rapeseed, fruit, clovers - Flavors: sweet honey with vegetal notes

Target Market(s)

affluent clientele looking for natural products, good for health, ...

Industry/Entity Type

Agriculture

Font styles to use
Decorative
Script
Other font styles liked:
• à la libre appréciation du designer, tant que c'est moderne et élégant

Requirements
Must have
• All text must be in French / A main label and a round label on the lid of the jar. Gilding (preferably on a black background). An image accompanying the text. Gold on a black background
Nice to have
• Elegant and modern design Elegant and modern design
Should not have
• Do not load too much the main label, it must remain uncluttered

```html
<!DOCTYPE html>
<html lang="fr">
<head>
<meta charset="utf-8">
<title>Le miel du Waldhofen – étiquette</title>
<link rel="stylesheet" href="https://fonts.googleapis.com/css2?family=Cormorant+Garamond:wght@500&family=Cinzel:wght@400&family=Oswald:wght@400&display=swap">
<style>
  :root {
    --gold: #b39a5f;
    --gold-light: #d4bd85;
    --black: #231f20;
    --grey: #9b9b9b;
    --paper: #ffffff;
  }
  * { margin: 0; padding: 0; box-sizing: border-box; }
  html, body { width: 1200px; height: 893px; overflow: hidden; background: var(--paper); }
  .board { position: relative; width: 1200px; height: 893px; }
  .shapes { position: absolute; left: 0; top: 0; width: 1200px; height: 893px; }

  .text { position: absolute; text-align: center; white-space: nowrap; }
  .serif { font-family: "Cormorant Garamond", serif; font-weight: 500; }
  .caps { font-family: "Cinzel", serif; font-weight: 400; }

  /* brand mark */
  .brand__lead { left: 462px; width: 300px; top: 128px; font-size: 35px; line-height: 1; color: var(--grey); }
  .brand__name { left: 432px; width: 360px; top: 180px; font-size: 66px; line-height: 1; color: var(--grey); }
  .brand__bee { position: absolute; border-radius: 50%; background: radial-gradient(circle, #cfcfcf 0%, #eeeeee 100%); }
  .brand__bee--top { left: 742px; top: 120px; width: 56px; height: 44px; }
  .brand__bee--bottom { left: 580px; top: 258px; width: 60px; height: 62px; }

  /* flat label */
  .label__flora {
    position: absolute; left: 80px; top: 412px; width: 536px; height: 146px;
    background: linear-gradient(180deg, rgba(179,154,95,0.08) 0%, rgba(179,154,95,0.38) 100%);
  }
  .label__lead { left: 196px; width: 300px; top: 488px; font-size: 31px; line-height: 1; color: var(--gold); }
  .label__name { left: 176px; width: 340px; top: 532px; font-size: 58px; line-height: 1; color: var(--gold); }
  .label__bee {
    position: absolute; left: 318px; top: 598px; width: 56px; height: 50px; border-radius: 50%;
    background: radial-gradient(circle, rgba(179,154,95,0.6) 0%, rgba(179,154,95,0.12) 100%);
  }
  .label__beeside {
    position: absolute; left: 452px; top: 480px; width: 48px; height: 44px; border-radius: 50%;
    background: radial-gradient(circle, rgba(179,154,95,0.6) 0%, rgba(179,154,95,0.12) 100%);
  }
  .label__tagline { left: 76px; width: 540px; top: 698px; font-size: 19px; letter-spacing: 1.3px; line-height: 1.2; color: var(--gold); }
  .label__weight { left: 76px; width: 540px; top: 728px; font-size: 15px; letter-spacing: 1.5px; line-height: 1.2; color: var(--gold); }

  /* ink swatches */
  .swatches { position: absolute; left: 290px; top: 830px; display: flex; gap: 62px; }
  .swatch { display: flex; align-items: center; gap: 8px; }
  .swatch__chip { width: 25px; height: 25px; }
  .swatch__chip--gold { background: var(--gold); }
  .swatch__chip--black { background: #000; }
  .swatch__name { font-family: "Oswald", sans-serif; font-size: 11px; letter-spacing: 0.3px; color: #000; }
</style>
</head>
<body>
<main class="board">

  <div class="label__flora" role="img" aria-label="Motifs floraux champêtres dorés"></div>

  <svg class="shapes" viewBox="0 0 1200 893" aria-hidden="true">
    <!-- brand badge frame -->
    <polygon points="512,66 712,66 772,205 712,344 512,344 452,205"
             fill="none" stroke="#9b9b9b" stroke-width="4" stroke-linejoin="round"/>
    <!-- label band and body -->
    <rect x="76" y="558" width="540" height="20" fill="#b39a5f"/>
    <path d="M76 578 H616 V754 Q616 782 588 782 H104 Q76 782 76 754 Z" fill="#231f20"/>
    <!-- label badge -->
    <polygon points="252,422 442,422 514,546 442,674 252,674 180,546"
             fill="#231f20" stroke="#231f20" stroke-width="8" stroke-linejoin="round"/>
    <polygon points="258,432 436,432 502,546 436,664 258,664 192,546"
             fill="none" stroke="#b39a5f" stroke-width="2.5" stroke-linejoin="round"/>
  </svg>

  <section class="brand">
    <div class="brand__bee brand__bee--top" role="img" aria-label="Gravure d'abeille en vol"></div>
    <p class="text serif brand__lead">Le miel du</p>
    <p class="text serif brand__name">Waldhofen</p>
    <div class="brand__bee brand__bee--bottom" role="img" aria-label="Gravure d'abeille posée"></div>
  </section>

  <section class="label">
    <div class="label__beeside" role="img" aria-label="Gravure d'abeille dorée en vol"></div>
    <p class="text serif label__lead">Le miel du</p>
    <p class="text serif label__name">Waldhofen</p>
    <div class="label__bee" role="img" aria-label="Gravure d'abeille dorée"></div>
    <p class="text caps label__tagline">MIEL DOUX AUX NOTES VÉGÉTALES</p>
    <p class="text caps label__weight">- 500 g -</p>
  </section>

  <footer class="swatches">
    <div class="swatch"><span class="swatch__chip swatch__chip--gold"></span><span class="swatch__name">GOLD INK</span></div>
    <div class="swatch"><span class="swatch__chip swatch__chip--black"></span><span class="swatch__name">BLACK</span></div>
  </footer>

</main>
</body>
</html>
```